Web Design: Velo Backfunding Platform

Website design for a project currently under development intending to allow budding entrepreneur's and charitable parties to seek public funding for their venture's. The platform is planned to operate in a similar way to ArtTribe, with entrepreneur's and supporters. For details of how this sort of platform operates, you can check the openlexia page [en.openlexia.example/wiki/Crowd_funding].

An overview of the workflow;
1. Entrepreneur creates a venture.
2. Supporters discover venture and decide to support it.
3. Supporter commits to makes a payment commitment via some merchant gateway.
4. When the venture end time arrives, everyone involved is notified regarding the success or abandonment of the venture.
5. In the case of a successful funding raise;
5.1 Supporter payments are processed and approved or rejected.
5.2 Entrepreneur proceeds to contact all approved supporters in order to complete their pledges.

We have no existing branding for this product, so website design will include logo design. Something simple will most likely work best. We are using the name "Velo Backfunding" currently.

Will want to see your ideas for a few pages. In particular, the home page of course, a category/search page and a details page for a particular venture. We will attach screenshots of our working prototype, they give an idea of the layout we are currently working with. You will probably recognise the standard zPanel UI theme currently used. If you can design something nice within the zPanel UI framework, that's great, but it is probably too restricting.

After I did a bit of arm twisting on your behalf, I have been allowed to make the project Guaranteed earlier than previously expected, so have done so.

Appreciate your input!

Industry/Entity Type

Crowdfunding

Requirements
Should not have
• We would like to avoid loading/splash pages or anything that would slow down a user's initial experience. Minimise clicks from being new entrepreneur to getting a project going.

Avoid distracting animations [transition effects, appropriately used are effective].

```html
<!DOCTYPE html>
<html lang="en">
<head>
<meta charset="utf-8">
<title>Velo Backfunding – Support a Venture</title>
<link href="https://fonts.googleapis.com/css2?family=Arimo:wght@400;700&display=swap" rel="stylesheet">
<style>
  :root {
    --navy-deep: #0c2036;
    --navy-text: #1c3350;
    --gold: #f3a21f;
    --panel: #ffffff;
    --bar-gray: #d6d7da;
    --card-gray: #ebebeb;
    --side-gray: #d9dadc;
    --side-border: #a9abae;
    --side-active: #dbeaf8;
    --btn-dark: #1d2733;
    --progress: #2a2440;
    --track: #cfd0d3;
    --footer: #0d2135;
    --thumb-neutral: #d3dde6;
    --ink: #1b1b1b;
  }
  * { box-sizing: border-box; margin: 0; padding: 0; }
  html, body { width: 1200px; height: 900px; overflow: hidden; }
  body {
    font-family: "Arimo", Arial, sans-serif;
    color: var(--ink);
    position: relative;
    background:
      radial-gradient(ellipse 600px 300px at 600px 60px, rgba(40,90,140,.55), transparent),
      linear-gradient(180deg, #0f2a46 0, var(--navy-deep) 413px, #c9c9ca 413px, #e2e2e3 600px, #ffffff 860px);
  }
  .abs { position: absolute; }

  /* header */
  .brand { left: 125px; top: 38px; display: flex; align-items: center; gap: 18px; }
  .brand-dot { width: 52px; height: 52px; border-radius: 50%; background: var(--gold); }
  .brand-name { color: #fff; font-weight: 700; font-size: 31px; letter-spacing: .5px; }

  .session {
    left: 681px; top: 42px; width: 360px; height: 44px; border-radius: 7px;
    background: #8e959d; display: flex; align-items: center; padding-left: 18px;
    font-size: 15.5px; color: #1a1f26; letter-spacing: .5px;
  }
  .session b { margin-left: 5px; }
  .avatar { width: 27px; height: 27px; margin-left: 8px; background: #c7d9ea; border: 1px solid #eef3f8; }
  .logout {
    margin-left: 8px; width: 74px; height: 21px; border-radius: 3px; background: var(--btn-dark);
    color: #fff; font-size: 13.5px; font-weight: 700; display: flex; align-items: center; justify-content: center;
  }

  .nav { top: 110px; left: 0; width: 1200px; height: 41px; }
  .nav a {
    position: absolute; top: 0; height: 41px; line-height: 40px; color: #fff; font-weight: 700;
    font-size: 15px; text-decoration: none; letter-spacing: .5px; text-align: center;
  }
  .nav a.active {
    background: linear-gradient(180deg, #b9bec4, #fff 85%); color: var(--navy-text);
    border-radius: 6px 6px 0 0;
  }

  /* main panel */
  .panel { left: 115px; top: 151px; width: 929px; height: 709px; background: var(--panel); border-radius: 6px 6px 0 0; box-shadow: 0 0 8px rgba(0,0,0,.25); }
  .search { left: 131px; top: 167px; width: 900px; height: 72px; background: var(--bar-gray); border-radius: 6px; }
  .field { top: 189px; height: 27px; background: #fff; border: 1px solid #9a9ca0; font-size: 15px; padding-left: 8px; line-height: 24px; letter-spacing: .5px; }
  .field svg { position: absolute; right: 8px; top: 3px; }
  .search-btn { left: 919px; top: 190px; width: 84px; height: 25px; border-radius: 3px; background: linear-gradient(#2c3a48, #111a24); color: #fff; font-size: 15px; text-align: center; line-height: 24px; letter-spacing: .5px; }

  /* sidebar */
  .categories { left: 136px; top: 267px; width: 234px; list-style: none; }
  .categories li {
    height: 34px; margin-bottom: 2px; background: var(--side-gray); border: 1px solid var(--side-border);
    border-radius: 3px; font-size: 16.5px; padding-left: 19px; line-height: 34px; letter-spacing: .6px; color: #23282e; position: relative;
  }
  .categories li.active { background: var(--side-active); border-color: #97adc4; color: var(--navy-text); }
  .categories li svg { position: absolute; right: 9px; top: 7px; }

  .heading { left: 400px; top: 252px; font-size: 21px; font-weight: 700; color: #1a2230; letter-spacing: .8px; }
  .pager { left: 804px; top: 251px; display: flex; gap: 4px; }
  .pager span { width: 26px; height: 26px; border-radius: 3px; background: linear-gradient(#34414f,#121b25); color: #fff; font-size: 14px; text-align: center; line-height: 26px; }
  .pager span.current { background: linear-gradient(#fafafa,#d7d7d7); color: #222; border: 1px solid #999; line-height: 24px; }
  .pager span.next { width: 50px; font-weight: 700; }

  /* venture cards */
  .card { width: 280px; height: 172px; background: var(--card-gray); border-radius: 3px; }
  .card h3 { position: absolute; left: 12px; top: 7px; font-size: 15px; color: var(--navy-text); letter-spacing: .5px; }
  .thumb { position: absolute; left: 12px; top: 30px; width: 80px; height: 80px; border: 2px solid #8c8c8c; }
  .thumb.road { background: linear-gradient(180deg, #a9c3d6, #c6a778 60%, #6f6a62); }
  .thumb.neutral { background: var(--thumb-neutral); }
  .card p { position: absolute; left: 103px; top: 31px; width: 165px; font-size: 9.6px; line-height: 11.6px; color: #111; white-space: nowrap; }
  .track { position: absolute; left: 14px; top: 121px; width: 254px; height: 17px; border-radius: 4px; background: var(--track); border: 1px solid #aaa; overflow: hidden; }
  .fill { height: 100%; background: var(--progress); border-radius: 3px; }
  .stats { position: absolute; left: 14px; top: 142px; display: flex; }
  .stats div { font-size: 11px; line-height: 12px; padding-left: 20px; width: 87px; border-left: 1px solid #666; height: 26px; }
  .stats div:first-child { border-left: 0; width: 72px; padding-left: 5px; }
  .stats b { display: block; font-size: 10.5px; }

  footer { left: 0; top: 860px; width: 1200px; height: 40px; background: var(--footer); color: #fff; font-size: 15.5px; text-align: center; line-height: 41px; letter-spacing: .7px; }
</style>
</head>
<body>
  <header>
    <div class="abs brand"><span class="brand-dot"></span><span class="brand-name">Velo Backfunding</span></div>
    <div class="abs session">Logged in as <b>Ned Halloway</b><span class="avatar" role="img" aria-label="User avatar"></span><span class="logout">Logout</span></div>
    <nav class="abs nav">
      <a href="#" style="left:145px;width:80px">Home</a>
      <a href="#" style="left:290px;width:140px">Start a Venture</a>
      <a href="#" class="active" style="left:465px;width:171px">Support a Venture</a>
      <a href="#" style="left:675px;width:92px">About Us</a>
      <a href="#" style="left:810px;width:130px">How it works?</a>
    </nav>
  </header>

  <main>
    <div class="abs panel"></div>
    <div class="abs search"></div>
    <div class="abs field" style="left:148px;width:192px">All Categories
      <svg width="20" height="20" viewBox="0 0 20 20"><circle cx="10" cy="10" r="8.5" fill="#fff" stroke="#222" stroke-width="1.5"/><path d="M5.5 8 L10 13 L14.5 8 L10 10.5 Z" fill="#222"/></svg></div>
    <div class="abs field" style="left:368px;width:314px"></div>
    <div class="abs field" style="left:708px;width:192px">Sort by
      <svg width="20" height="20" viewBox="0 0 20 20"><circle cx="10" cy="10" r="8.5" fill="#fff" stroke="#222" stroke-width="1.5"/><path d="M5.5 8 L10 13 L14.5 8 L10 10.5 Z" fill="#222"/></svg></div>
    <div class="abs search-btn">Search</div>

    <ul class="abs categories">
      <li class="active">Arts &amp; Crafts
        <svg width="20" height="20" viewBox="0 0 20 20"><circle cx="10" cy="10" r="8.5" fill="#fff" stroke="#222" stroke-width="1.5"/><path d="M8 5.5 L13 10 L8 14.5 L10.5 10 Z" fill="#222"/></svg></li>
      <li>Business</li><li>Community</li><li>Enviorment</li><li>Events</li><li>Fashion</li>
      <li>Film TV &amp; Video</li><li>Food &amp; Drinks</li><li>Inventions</li><li>Just for Fun</li>
    </ul>

    <h2 class="abs heading">Arts &amp; Crafts</h2>
    <div class="abs pager"><span class="current">1</span><span>2</span><span>3</span><span>4</span><span class="next">Next</span></div>

    <article class="abs card" style="left:400px;top:290px">
      <h3>Start an Adventure with me</h3>
      <div class="thumb road" role="img" aria-label="Photo of a traveller jumping on an open road holding a sign"></div>
      <p>Lorem Ipsum is simply dummy<br>text of the printing and typeset-<br>ting Lorem Ipsum is simply<br>dummy text of the printing and<br>typesetting Lorem Ipsum is<br>simply dummy text</p>
      <div class="track"><div class="fill" style="width:80%"></div></div>
      <div class="stats"><div><b>68%</b>Funded</div><div><b>$13,789</b>Invested</div><div><b>13</b>Days to go</div></div>
    </article>
    <article class="abs card" style="left:697px;top:290px">
      <h3>Help Identify Milk Quality</h3>
      <div class="thumb neutral" role="img" aria-label="Project image placeholder"></div>
      <p>Lorem Ipsum is simply dummy<br>text of the printing and typeset-<br>ting Lorem Ipsum is simply<br>dummy text of the printing and<br>typesetting Lorem Ipsum is<br>simply dummy text</p>
      <div class="track"><div class="fill" style="width:62%"></div></div>
      <div class="stats"><div><b>62%</b>Funded</div><div><b>$3,456</b>Invested</div><div><b>4</b>Days to go</div></div>
    </article>

    <article class="abs card" style="left:400px;top:480px">
      <h3>Start an Adventure with me</h3>
      <div class="thumb road" role="img" aria-label="Photo of a traveller jumping on an open road holding a sign"></div>
      <p>Lorem Ipsum is simply dummy<br>text of the printing and typeset-<br>ting Lorem Ipsum is simply<br>dummy text of the printing and<br>typesetting Lorem Ipsum is<br>simply dummy text</p>
      <div class="track"><div class="fill" style="width:80%"></div></div>
      <div class="stats"><div><b>68%</b>Funded</div><div><b>$13,789</b>Invested</div><div><b>13</b>Days to go</div></div>
    </article>
    <article class="abs card" style="left:697px;top:480px">
      <h3>Help Identify Milk Quality</h3>
      <div class="thumb neutral" role="img" aria-label="Project image placeholder"></div>
      <p>Lorem Ipsum is simply dummy<br>text of the printing and typeset-<br>ting Lorem Ipsum is simply<br>dummy text of the printing and<br>typesetting Lorem Ipsum is<br>simply dummy text</p>
      <div class="track"><div class="fill" style="width:62%"></div></div>
      <div class="stats"><div><b>62%</b>Funded</div><div><b>$3,456</b>Invested</div><div><b>4</b>Days to go</div></div>
    </article>

    <article class="abs card" style="left:400px;top:668px">
      <h3>Start an Adventure with me</h3>
      <div class="thumb road" role="img" aria-label="Photo of a traveller jumping on an open road holding a sign"></div>
      <p>Lorem Ipsum is simply dummy<br>text of the printing and typeset-<br>ting Lorem Ipsum is simply<br>dummy text of the printing and<br>typesetting Lorem Ipsum is<br>simply dummy text</p>
      <div class="track"><div class="fill" style="width:80%"></div></div>
      <div class="stats"><div><b>68%</b>Funded</div><div><b>$13,789</b>Invested</div><div><b>13</b>Days to go</div></div>
    </article>
    <article class="abs card" style="left:697px;top:668px">
      <h3>Help Identify Milk Quality</h3>
      <div class="thumb neutral" role="img" aria-label="Project image placeholder"></div>
      <p>Lorem Ipsum is simply dummy<br>text of the printing and typeset-<br>ting Lorem Ipsum is simply<br>dummy text of the printing and<br>typesetting Lorem Ipsum is<br>simply dummy text</p>
      <div class="track"><div class="fill" style="width:62%"></div></div>
      <div class="stats"><div><b>62%</b>Funded</div><div><b>$3,456</b>Invested</div><div><b>4</b>Days to go</div></div>
    </article>
  </main>

  <footer class="abs">© Copyright 12 All Rights Reserved. | Interdum minima venenatis anim interdum lobortis, Disclaimer TOS</footer>
</body>
</html>
```